plumbers buisness card

A buisness card for a plumbing buisness
needs to have a water theme with navy blue, light blue and white
with an image of either a water drop, pipes, tools or something relating to plumbing and incorperating my buisness name as a logo

"Talcott Plumbing" is the words that need to stand out with "& gasfitting" to be smaller
Updates

spelling error on brief, "maintenance"
and also could you include my email m_talcott@nimbrel.com.au

Industry/Entity Type

Plumbing

Contact Information for Business Card

Talcott Plumbing & Gasfitting

myles talcott
0492315806

specialising in
-new homes
-maitenance
-renovations

license no.
-73846

```html
<!DOCTYPE html>
<html lang="en">
<head>
<meta charset="utf-8">
<title>Talcott Plumbing &amp; Gasfitting – Business Card</title>
<link rel="stylesheet" href="https://fonts.googleapis.com/css2?family=Cabin:wght@400;600&display=swap">
<style>
  :root {
    --page-bg: #5a5a5a;
    --card-navy: #151d2c;
    --card-navy-deep: #0f1522;
    --text-white: #ffffff;
    --text-soft: #d9dee6;
    --accent-cyan: #3ec6e3;
    --icon-tan: #cbb89b;
    --body-font: "Cabin", sans-serif;
  }
  * { margin: 0; padding: 0; box-sizing: border-box; }
  html, body {
    width: 1200px;
    height: 949px;
    overflow: hidden;
    background: var(--page-bg);
    font-family: var(--body-font);
  }
  .business-card {
    position: absolute;
    left: 75px;
    top: 174px;
    width: 1050px;
    height: 600px;
    background: linear-gradient(160deg, var(--card-navy) 0%, var(--card-navy-deep) 100%);
    color: var(--text-white);
  }
  .brand {
    position: absolute;
    right: 70px;
    top: 72px;
    text-align: right;
    font-weight: 600;
    color: var(--text-white);
    line-height: 1;
  }
  .brand-line {
    display: flex;
    align-items: center;
    justify-content: flex-end;
    gap: 12px;
    font-size: 50px;
    letter-spacing: -0.5px;
    text-transform: uppercase;
  }
  .brand-mark {
    width: 34px;
    height: 34px;
    border-radius: 50%;
    background: var(--text-white);
    flex: none;
  }
  .brand-sub {
    display: block;
    margin-top: 8px;
    font-size: 38px;
    font-weight: 400;
    text-transform: uppercase;
  }
  .license {
    position: absolute;
    right: 75px;
    top: 200px;
    font-size: 26px;
    color: var(--text-white);
  }
  .contact {
    position: absolute;
    left: 80px;
    top: 362px;
  }
  .contact-name {
    font-size: 41px;
    font-weight: 400;
    line-height: 1.1;
  }
  .contact-role {
    font-size: 31px;
    color: var(--accent-cyan);
    margin-top: 2px;
  }
  .contact-phone {
    display: flex;
    align-items: center;
    gap: 12px;
    font-size: 38px;
    margin-top: 6px;
  }
  .contact-phone svg { width: 44px; height: 44px; flex: none; }
  .contact-email {
    font-size: 26px;
    color: var(--text-soft);
    margin-top: 10px;
  }
  .services {
    position: absolute;
    right: 70px;
    top: 350px;
    text-align: right;
    font-size: 30px;
    line-height: 1.4;
  }
  .services-title { margin-right: 30px; }
  .services-list { list-style: none; }
  .services-list li {
    display: flex;
    align-items: center;
    justify-content: flex-end;
    gap: 14px;
  }
  .services-list svg { width: 14px; height: 20px; flex: none; }
</style>
</head>
<body>
  <main class="business-card">
    <header class="brand">
      <span class="brand-line"><span class="brand-mark"></span>Talcott Plumbing</span>
      <span class="brand-sub">and Gasfitting</span>
    </header>
    <p class="license">License no. -73846</p>

    <section class="contact">
      <h1 class="contact-name">Myles Talcott</h1>
      <p class="contact-role">Owner</p>
      <p class="contact-phone">
        <svg viewBox="0 0 44 44" aria-hidden="true">
          <circle cx="22" cy="22" r="19" fill="none" stroke="var(--icon-tan)" stroke-width="2.5"/>
          <path d="M15 12c2-1 3 0 4 2l1 3c.5 1.5-.5 2.5-1.5 3 1 3 3.5 5.5 6.5 6.5.5-1 1.5-2 3-1.5l3 1c2 1 3 2 2 4-1 2-3 3-5 2.5C20 30 14 24 12.5 17 12 15 13 13 15 12z" fill="none" stroke="var(--icon-tan)" stroke-width="2.2" stroke-linejoin="round"/>
        </svg>
        0492315806
      </p>
      <p class="contact-email">m_talcott@nimbrel.com.au</p>
    </section>

    <section class="services">
      <p class="services-title">Specialising in</p>
      <ul class="services-list">
        <li>new homes<svg viewBox="0 0 14 20" aria-hidden="true"><path d="M7 1C5 6 1 9 1 13a6 6 0 0 0 12 0C13 9 9 6 7 1z" fill="var(--accent-cyan)"/></svg></li>
        <li>maintenance<svg viewBox="0 0 14 20" aria-hidden="true"><path d="M7 1C5 6 1 9 1 13a6 6 0 0 0 12 0C13 9 9 6 7 1z" fill="var(--accent-cyan)"/></svg></li>
        <li>renovations<svg viewBox="0 0 14 20" aria-hidden="true"><path d="M7 1C5 6 1 9 1 13a6 6 0 0 0 12 0C13 9 9 6 7 1z" fill="var(--accent-cyan)"/></svg></li>
      </ul>
    </section>
  </main>
</body>
</html>
```